8" x 11" One Page Flyer for Fence Installation Company

We are looking to promote our business with a new flyer that would be handed out in person to people or put at their mailbox/door at their homes. The flyer needs to be creative and attention-grabbing. I have attached some of our previous flyers and our website information. Do not call or email regarding the flyer. We want the flyer to look professional but also friendly. One page, NOT folded. You can use images from our website at www.MyBraxtonYard.com or our Facebook page at www.Facebook.com/HollowbrookRailsBKT. We are flexible with what photos you can use but there must be photos of OUR fences on the flyer. More photos specifically can also be provided. Colors need to be suitable for a flyer printed on canary yellow in color paper OR white paper.

Target Market(s)

Homeowners that need a new fence

Industry/Entity Type

Construction

Font styles to use
Sans Serif
Other font styles liked:
• HD Colton

Colors
0054AA
0677BA
7BADD7
CADEEF
E8F1F8
0094D4
00A9DD
6FCCEA
C7EBF8
E9F6FB

Requirements
Must have
• Our fence photos - mostly wood fence photos (different designs), SIZE SHOULD BE LETTER SIZE 8" x 11"
Nice to have
• A nice bible verse featured at the bottom of the flyer.
Should not have
• DO NOT COPY THE WEBSITE FORMAT, I WANT SOMETHING UNIQUE. Other people's fence photos, they must all come from our website or facebook page

```html
<!DOCTYPE html>
<html lang="en">
<head>
<meta charset="utf-8">
<title>Hollowbrook Rails Flyer</title>
<link rel="stylesheet" href="https://fonts.googleapis.com/css2?family=Saira:wght@400;500;600;700;800;900&family=Kaushan+Script&family=Poppins:wght@400;500;600&display=swap">
<style>
:root{
  --blue:#2a82cc;
  --black:#1b1b1b;
  --orange:#e69a35;
  --orange-dark:#c97d1c;
  --white:#ffffff;
  --backdrop:#808080;
  --brown:#54402f;
}
*{margin:0;padding:0;box-sizing:border-box}
html,body{width:1200px;height:1200px;overflow:hidden;background:var(--backdrop)}
.flyer{
  position:absolute;left:197px;top:45px;width:1298px;height:1785px;
  background:var(--white);overflow:hidden;
  transform:scale(0.6211);transform-origin:0 0;
  font-family:'Saira',sans-serif;
}
.shapes{position:absolute;left:0;top:0}
.abs{position:absolute;white-space:nowrap}
.brand-mark{left:88px;top:120px;width:120px;height:120px;background:var(--brown)}
.brand-name{left:241px;top:104px;font-size:50px;font-weight:700;color:var(--blue);line-height:1.1}
.brand-phone{left:239px;top:160px;font-size:54px;font-weight:800;color:#000;line-height:1.1}
.brand-tagline{left:241px;top:226px;font-size:19px;font-weight:500;color:#000}
.headline-top{left:60px;top:300px;font-size:130px;font-weight:900;color:var(--blue);line-height:1;letter-spacing:-1px}
.headline-main{left:60px;top:432px;font-size:172px;font-weight:900;color:var(--orange);line-height:1;letter-spacing:-2px}
.subline{left:67px;top:620px;font-size:38px;font-weight:500;color:#000}
.badge{position:absolute;transform:rotate(-9deg);font-weight:800;color:#000;display:flex;align-items:center;justify-content:center}
.badge-free{left:918px;top:478px;width:228px;height:108px;background:linear-gradient(180deg,#f3b964,var(--orange-dark));font-size:76px}
.badge-estimates{left:942px;top:570px;width:318px;height:96px;background:linear-gradient(180deg,#4a9ae0,#1f6fb8);font-size:58px}
.why{left:81px;top:728px;color:var(--white);line-height:1}
.why-big{font-size:66px;font-weight:400}
.why-small{font-size:44px;font-weight:400;margin-top:2px}
.pitch{left:417px;top:735px;font-size:41px;font-weight:400;color:var(--white);line-height:1.25}
.perk{position:absolute;display:flex;align-items:center;gap:18px;font-size:28px;font-weight:700;color:var(--white);white-space:nowrap}
.perk svg{width:22px;height:22px}
.showroom-title{left:75px;top:1508px;font-family:'Kaushan Script',cursive;font-size:64px;line-height:1.12;color:var(--blue)}
.showroom-title .warm{color:var(--orange)}
.hours-intro{left:668px;top:1520px;font-family:'Poppins',sans-serif;color:var(--blue)}
.hours-intro .line-one{height:46px;font-size:25px;display:flex;align-items:baseline;gap:8px}
.hours-intro strong{font-family:'Saira',sans-serif;font-size:40px;font-weight:800;line-height:46px}
.hours-intro .line-two{font-size:25px;line-height:34px}
.hours-box{left:659px;top:1610px;width:563px;height:50px;background:var(--blue);color:var(--white);font-family:'Poppins',sans-serif;font-size:23px;display:flex;align-items:center;justify-content:center}
.footer{position:absolute;left:0;top:1693px;width:1298px;height:92px;background:var(--black);display:flex;align-items:center;justify-content:center;gap:14px;color:var(--white);font-size:31px;font-weight:700}
.footer .item{display:flex;align-items:center;gap:12px}
.footer .divider{width:3px;height:46px;background:var(--white)}
.footer svg{width:22px;height:22px}
</style>
</head>
<body>
<div class="flyer">
  <svg class="shapes" width="1298" height="1785" viewBox="0 0 1298 1785">
    <defs>
      <linearGradient id="yard" x1="0" y1="0" x2="0" y2="1">
        <stop offset="0" stop-color="#8aa0a8"/>
        <stop offset="0.35" stop-color="#7f9a5c"/>
        <stop offset="1" stop-color="#6d7a45"/>
      </linearGradient>
      <linearGradient id="wood" x1="0" y1="0" x2="1" y2="1">
        <stop offset="0" stop-color="#d9bf8a"/>
        <stop offset="1" stop-color="#a88a5a"/>
      </linearGradient>
      <clipPath id="flyer-clip"><rect width="1298" height="1785"/></clipPath>
    </defs>
    <g clip-path="url(#flyer-clip)">
      <path d="M0 700 L700 700 C920 700 1150 590 1298 480 L1298 1180 L0 1180 Z" fill="var(--black)"/>
      <circle cx="1043" cy="257" r="315" fill="var(--blue)"/>
      <circle cx="1043" cy="257" r="302" fill="url(#yard)" role="img" aria-label="Photo of a black aluminium fence installed around a grassy backyard"/>
      <path d="M0 700 L398 703 C390 800 340 885 160 888 L0 885 Z" fill="var(--blue)"/>
      <path d="M0 885 L160 888 C340 885 390 800 398 703" fill="none" stroke="var(--white)" stroke-width="4"/>
      <path d="M0 887 C300 880 900 868 1298 870 L1298 1135 C900 1110 400 1140 0 1170 Z" fill="var(--blue)"/>
      <path d="M0 1170 C400 1140 900 1110 1298 1135 L1298 1180 C900 1130 400 1150 0 1180 Z" fill="var(--black)"/>
      <path d="M0 1180 C400 1150 900 1130 1298 1180 L1298 1785 L0 1785 Z" fill="var(--white)"/>
      <g stroke="var(--blue)" stroke-width="3">
        <circle cx="177" cy="1324" r="150" fill="url(#wood)" role="img" aria-label="Photo of a split rail wood fence with wire mesh"/>
        <circle cx="493" cy="1324" r="150" fill="url(#wood)" role="img" aria-label="Photo of a tall wooden privacy fence"/>
        <circle cx="810" cy="1324" r="150" fill="url(#wood)" role="img" aria-label="Photo of a wooden picket fence beside a house"/>
        <circle cx="1126" cy="1324" r="150" fill="url(#wood)" role="img" aria-label="Photo of a wooden gate with black hinges"/>
      </g>
      <path d="M553 1517 C575 1467 640 1467 675 1502" fill="none" stroke="var(--orange)" stroke-width="6" stroke-linecap="round"/>
      <path d="M650 1505 L676 1504 L672 1481" fill="none" stroke="var(--orange)" stroke-width="6" stroke-linecap="round" stroke-linejoin="round"/>
    </g>
  </svg>

  <div class="abs brand-mark"></div>
  <div class="abs brand-name">Hollowbrook Rails</div>
  <div class="abs brand-phone">555-014-2287</div>
  <div class="abs brand-tagline">“Because Good Fences Make Good Neighbours”</div>

  <div class="abs headline-top">WE BUILD</div>
  <div class="abs headline-main">FENCES....</div>
  <div class="abs subline">And we would love to build your fence too!</div>

  <div class="badge badge-free">Free</div>
  <div class="badge badge-estimates">Estimates</div>

  <div class="abs why"><div class="why-big">WHY</div><div class="why-small">CHOOSE US?</div></div>
  <div class="abs pitch">Beautiful, professionally installed fences at<br>affordable prices!</div>

  <div class="perk" style="left:65px;top:913px"><svg viewBox="0 0 22 22"><path d="M2 12 L8 18 L20 3" fill="none" stroke="#fff" stroke-width="3.5"/></svg>Professional Installation</div>
  <div class="perk" style="left:462px;top:910px"><svg viewBox="0 0 22 22"><path d="M2 12 L8 18 L20 3" fill="none" stroke="#fff" stroke-width="3.5"/></svg>Concrete in EVERY Post</div>
  <div class="perk" style="left:846px;top:910px"><svg viewBox="0 0 22 22"><path d="M2 12 L8 18 L20 3" fill="none" stroke="#fff" stroke-width="3.5"/></svg>HOA Submission Assistance</div>
  <div class="perk" style="left:65px;top:980px"><svg viewBox="0 0 22 22"><path d="M2 12 L8 18 L20 3" fill="none" stroke="#fff" stroke-width="3.5"/></svg>Lifetime Workmanship Warranty</div>
  <div class="perk" style="left:603px;top:980px"><svg viewBox="0 0 22 22"><path d="M2 12 L8 18 L20 3" fill="none" stroke="#fff" stroke-width="3.5"/></svg>Experienced Installation Teams</div>
  <div class="perk" style="left:65px;top:1047px"><svg viewBox="0 0 22 22"><path d="M2 12 L8 18 L20 3" fill="none" stroke="#fff" stroke-width="3.5"/></svg>Quality Workmanship &amp; Materials</div>
  <div class="perk" style="left:603px;top:1047px"><svg viewBox="0 0 22 22"><path d="M2 12 L8 18 L20 3" fill="none" stroke="#fff" stroke-width="3.5"/></svg>FREE Gate Adjustments for LIFE</div>

  <div class="abs showroom-title">Visit our <span class="warm">indoor &amp;</span><br><span class="warm">outdoor</span> showroom!</div>
  <div class="abs hours-intro">
    <div class="line-one">Our outdoor showroom is <strong>open 24/7,</strong></div>
    <div class="line-two">while our indoor showroom and office is open</div>
  </div>
  <div class="abs hours-box">Monday - Thurs 9AM - 3PM, Friday 9AM - 1PM</div>

  <footer class="footer">
    <span class="item"><svg viewBox="0 0 22 22"><circle cx="11" cy="11" r="9" fill="none" stroke="var(--orange)" stroke-width="2.5"/><path d="M2 11 H20 M11 2 C6 7 6 15 11 20 C16 15 16 7 11 2" fill="none" stroke="var(--orange)" stroke-width="2"/></svg>www.MyBraxtonYard.com</span>
    <span class="divider"></span>
    <span class="item"><svg viewBox="0 0 22 22"><path d="M5 2 L9 6 L7 9 C8 12 10 14 13 15 L16 13 L20 17 L17 20 C9 19 3 13 2 5 Z" fill="var(--orange)"/></svg>555-014-2287</span>
    <span class="divider"></span>
    <span class="item"><svg viewBox="0 0 22 22"><rect x="1" y="4" width="20" height="14" fill="var(--orange)"/><path d="M1 4 L11 12 L21 4" fill="none" stroke="var(--black)" stroke-width="2"/></svg>office@mybraxtonyard.com</span>
  </footer>
</div>
</body>
</html>
```